"You CAN Relax on Your Own Savings!" book cover for 80 page or so book.

Need a book cover that stands out on Bookvale, so highly engaging colors, need to reflect optimism, hope and determination. Go to Bookvale, type my name in and see the covers for the three other books I had written.

There's a lot of negativity and fear for Americans looking at retirement. Yet, they don't need that fear, my book tells them why they can be confident in their ability to retire.

There will be NO spine writing for the book, too small.

Target Market(s)

stressed out people in their 50s and 60s. This book appeals to working people, not high end, wealthy types.

Industry/Entity Type

Financial Planning

Colors

Designer to choose colors to be used in the design.

Requirements
Must have
• Needs to reflect simplicity in action.
• Please spell out my full name, GREG MALTHORPE, at the bottom of the cover.
Nice to have
• if there is anyway to put a picture of an RV (Recreational Vehicle) that would be great.
Should not have
• Do NOT want to be the stodgy, typical financial planning literature out there. No guy in a suit and tie. No one sitting on a beach.
• Do not want my face on the cover either. (On the back yes.)

```html
<!DOCTYPE html>
<html lang="en">
<head>
<meta charset="utf-8">
<title>You CAN Relax on Your Own Savings! — Greg Malthorpe</title>
<link href="https://fonts.googleapis.com/css2?family=Cinzel:wght@400;600;700&family=Cormorant+Garamond:wght@600&display=swap" rel="stylesheet">
<style>
  :root {
    --cover-bg: #f7f7f8;
    --title-blue: #155d9c;
    --author-blue: #1d3f7c;
    --url-ink: #1a1a1a;
    --art-light: #ffffff;
    --art-body: #eceef0;
    --art-trim: #c9cdd2;
  }
  html, body {
    margin: 0;
    padding: 0;
    width: 790px;
    height: 1200px;
    overflow: hidden;
    background: var(--cover-bg);
  }
  .cover {
    position: relative;
    width: 790px;
    height: 1200px;
    background: var(--cover-bg);
    overflow: hidden;
  }
  .title {
    margin: 0;
    font-family: "Cinzel", serif;
    font-weight: 700;
    color: var(--title-blue);
    text-align: center;
  }
  .title span {
    position: absolute;
    left: 0;
    width: 790px;
    display: block;
    line-height: 1;
    white-space: nowrap;
  }
  .title-lead   { top: 40px;  font-size: 106px; }
  .title-key    { top: 134px; font-size: 170px; letter-spacing: 2px; }
  .title-link   { top: 306px; font-size: 58px; font-weight: 600; }
  .title-close  { top: 375px; font-size: 50px; font-weight: 600; letter-spacing: 1px; }
  .cover-art {
    position: absolute;
    left: 24px;
    top: 564px;
    width: 744px;
    height: 504px;
    background:
      radial-gradient(ellipse 46% 8% at 50% 84%, rgba(150,156,164,0.35) 0%, rgba(150,156,164,0) 100%),
      radial-gradient(ellipse 40% 30% at 50% 52%, var(--art-body) 0%, var(--art-body) 55%, rgba(236,238,240,0) 100%),
      linear-gradient(180deg, var(--art-light) 0%, var(--art-light) 100%);
  }
  .author {
    position: absolute;
    left: 0;
    top: 1076px;
    width: 790px;
    text-align: center;
    font-family: "Cinzel", serif;
    font-weight: 400;
    font-size: 44px;
    letter-spacing: 12px;
    text-indent: 12px;
    color: var(--author-blue);
    line-height: 1;
    margin: 0;
    white-space: nowrap;
  }
  .site-url {
    position: absolute;
    left: 0;
    top: 1136px;
    width: 790px;
    text-align: center;
    font-family: "Cormorant Garamond", serif;
    font-weight: 600;
    font-size: 24px;
    color: var(--url-ink);
    line-height: 1;
    margin: 0;
  }
</style>
</head>
<body>
  <main class="cover">
    <h1 class="title">
      <span class="title-lead">YOU CAN</span>
      <span class="title-key">RELAX</span>
      <span class="title-link">ON</span>
      <span class="title-close">YOUR OWN SAVINGS!</span>
    </h1>
    <div class="cover-art" role="img" aria-label="White recreational vehicle motorhome with grey trim, shown three-quarter view on a plain white background"></div>
    <p class="author">GREG MALTHORPE</p>
    <p class="site-url">www.oakmerewealthplanning.com</p>
  </main>
</body>
</html>
```